Brenmoor Systems Website Revamp

We need a full website for the oil and gas sector to showcase our company and our technology/services we provide to larger corporations. We want our website represent innovation and identity.

Background:

We are a service based company that specializes in:

- well services, and
-permanent applications
**(Please be aware that these are two different aspects to the oil and gas sector, both of which we supply to our customers)

We provide a wide range of jet pump technologies to address under performing reservoirs or problematic well producing conditions. We have field operations currently in: Canada, Oman, and Australia with efforts currently underway to expand in other markets. Therefore are needing a website to help promote a better comprehension of what we do and how we can solve their well issues. We are looking for

1.) Identity;
2.) Emphasis on better comprehension of our services for our clients to relate to us as a solution to their needs;
3.) User friendly interface - but new and exciting in this digital age .

Some examples of websites we like:

http://quorvalinc.com/how-we-work/
http://www.tandrisystems.com/tandri-system/
https://mirelfield.com/

Videos of our technologies:

https://www.vidoquay.com/watch?v=Qm47TzxR2pa
https://www.vidoquay.com/watch?v=Lk8WnbeT5yc

Target Market(s)

Petroleum Industry Clients

Coding

Coded - Design and coding required

Number of Pages Required

5+ page

Colors

Designer to choose colors to be used in the design.

Requirements
Must have
• See Project Description, and feel free to contact us with any questions/inquiries!
Nice to have
• Our color scheme is generally 'blue', to depict jet pumps (our service). However, we are open to ideas and artistic interpretation. Grayscale/offset colors/highlight colors etc.

```html
<!DOCTYPE html>
<html lang="en">
<head>
<meta charset="utf-8">
<title>Brenmoor Systems</title>
<link href="https://fonts.googleapis.com/css2?family=Open+Sans:wght@400;600&family=Raleway:wght@300;400;500&family=Roboto:wght@300;400;500&family=Roboto+Slab:wght@400&display=swap" rel="stylesheet">
<style>
:root{
  --brand:#29a9e0;
  --brand-deep:#1a94d2;
  --ink:#444;
  --muted:#8a8a8a;
  --nav-bg:#dedede;
  --dark:#1e1e1e;
  --white:#fff;
}
*{margin:0;padding:0;box-sizing:border-box}
html,body{width:1200px;height:2507px;overflow:hidden;background:var(--white)}
body{position:relative;font-family:"Raleway",sans-serif;color:var(--ink)}

/* header */
.site-header{position:absolute;left:0;top:0;width:1200px;height:117px;background:var(--white)}
.brand{position:absolute;left:67px;top:34px;display:flex;align-items:center;gap:12px;font-family:"Roboto",sans-serif;font-weight:500;font-size:25px;color:var(--brand-deep)}
.brand-dot{width:16px;height:16px;border-radius:50%;background:var(--brand-deep)}
.header-photo{position:absolute;left:418px;top:13px;width:451px;height:84px;border:4px solid #cfcfcf;background:linear-gradient(180deg,#c9a27a 0%,#8c7a6a 45%,#5c5a58 100%)}
.social-squares{position:absolute;left:926px;top:28px;display:flex;gap:4px}
.social-squares span{width:46px;height:47px;background:#e3e3e3;display:block}

.main-nav{position:absolute;left:0;top:117px;width:1200px;height:57px;background:var(--nav-bg)}
.main-nav a{position:absolute;top:21px;font-family:"Open Sans",sans-serif;font-size:12.5px;color:#555;text-decoration:none;letter-spacing:.2px}
.main-nav a.active{color:var(--brand)}
.main-nav .caret{position:absolute;left:536px;top:47px;width:0;height:0;border-left:9px solid transparent;border-right:9px solid transparent;border-bottom:10px solid var(--brand)}

.hero{position:absolute;left:0;top:174px;width:1200px;height:503px;background:linear-gradient(180deg,#c4d4e4 0%,#a8b8c4 35%,#4b5a50 55%,#dfe6ee 75%,#eef2f6 100%)}
.hero-dots{position:absolute;left:530px;top:643px;display:flex;gap:6px}
.hero-dots span{width:9px;height:9px;border-radius:50%;background:rgba(255,255,255,.6)}
.hero-dots span:first-child{background:#fff}

/* section titles */
.section-title{position:absolute;left:0;width:1200px;text-align:center;font-family:"Roboto",sans-serif;font-weight:300;font-size:34px;letter-spacing:.5px}
.divider{position:absolute;left:430px;width:340px;height:20px}

.challenge-title{top:763px;color:var(--brand)}
.challenge-text{position:absolute;left:110px;top:850px;width:980px;text-align:center;font-weight:300;font-size:16.4px;letter-spacing:.35px;line-height:29px;color:#333}
.btn{position:absolute;display:flex;align-items:center;justify-content:center;font-family:"Roboto Slab",serif;font-size:14px}
.btn-solid{left:531px;top:1018px;width:137px;height:40px;background:var(--brand);color:var(--white);border:3px solid #d5eef9}

/* services band */
.services-band{position:absolute;left:0;top:1128px;width:1200px;height:247px;background:linear-gradient(160deg,#2b2b2b 0%,#1c1c1c 60%,#232323 100%)}
.service{position:absolute;top:1195px;width:260px;text-align:center;color:#e8e8e8;font-family:"Raleway",sans-serif;font-size:16.5px}
.service svg{display:block;margin:0 auto 12px}
.service-sep{position:absolute;top:1205px;width:1px;height:102px;background:#3c3c3c}

/* solution */
.solution{position:absolute;left:0;top:1375px;width:1200px;height:580px;background:linear-gradient(180deg,#1f9ee0 0%,#1596db 100%)}
.solution-title{top:1435px;color:var(--white)}
.solution-figure{position:absolute;left:92px;top:1567px;width:451px;height:308px;background:var(--white);padding:8px}
.solution-figure div{width:100%;height:100%;background:linear-gradient(180deg,#5d6f35 0%,#4d5a2f 25%,#6d6d70 40%,#3f3f44 100%)}
.solution-heading{position:absolute;left:582px;top:1561px;font-family:"Roboto Slab",serif;font-size:21px;color:var(--white)}
.solution-rule{position:absolute;left:582px;top:1598px;width:40px;height:3px;background:#0d5a86}
.solution-text{position:absolute;left:582px;width:528px;font-family:"Roboto",sans-serif;font-size:13.4px;line-height:22px;color:var(--white)}
.btn-outline{left:578px;top:1835px;width:139px;height:39px;border:2px solid var(--white);color:var(--white)}

/* follow */
.follow-label{position:absolute;left:232px;top:2011px;font-family:"Raleway",sans-serif;font-weight:300;font-size:33px;color:#a5a5a5}
.follow-circle{position:absolute;top:1995px;width:77px;height:77px;border-radius:50%;background:var(--muted)}

/* footer */
.site-footer{position:absolute;left:0;top:2114px;width:1200px;height:393px;background:var(--dark)}
.footer-heading{position:absolute;top:2165px;font-family:"Roboto",sans-serif;font-weight:500;font-size:13.5px;color:#dcdcdc;letter-spacing:.3px}
.footer-heading.faint{color:#2a2a2a}
.footer-rule{position:absolute;top:2192px;height:1px;background:#4a4a4a}
.footer-about{position:absolute;left:89px;top:2206px;width:240px;font-family:"Roboto",sans-serif;font-size:11.8px;line-height:23.5px;color:#cfcfcf}
.footer-links{position:absolute;list-style:none;font-family:"Roboto",sans-serif;font-size:11.8px;line-height:23.5px;color:#cfcfcf}
.newsletter-text{position:absolute;left:886px;top:2208px;width:238px;font-family:"Roboto",sans-serif;font-size:12.2px;line-height:21.5px;color:#cfcfcf;text-align:justify}
.email-field{position:absolute;left:886px;top:2316px;width:237px;height:34px;background:#e6e6e6;font-family:"Roboto",sans-serif;font-size:10px;color:#777;padding:11px 12px}
.subscribe{position:absolute;left:886px;top:2363px;width:75px;height:30px;background:var(--brand);color:var(--white);font-family:"Roboto",sans-serif;font-size:10px;display:flex;align-items:center;justify-content:center}
.to-top{position:absolute;left:1155px;top:2396px;width:36px;height:36px;background:#2f9ad6;display:flex;align-items:center;justify-content:center}
.copyright{position:absolute;left:89px;top:2469px;font-family:"Roboto",sans-serif;font-size:11.5px;color:#5c5c5c}
</style>
</head>
<body>

<header class="site-header">
  <div class="brand"><span class="brand-dot"></span>Brenmoor Systems</div>
  <div class="header-photo" role="img" aria-label="Photo of field equipment and pipework at sunset"></div>
  <div class="social-squares" aria-label="Social links">
    <span aria-label="Social network 1"></span>
    <span aria-label="Social network 2"></span>
    <span aria-label="Social network 3"></span>
    <span aria-label="Social network 4"></span>
  </div>
</header>

<nav class="main-nav">
  <a class="active" style="left:526px">HOME</a>
  <a style="left:601px">WHO WE ARE</a>
  <a style="left:719px">WHAT WE DO</a>
  <a style="left:837px">PRODUCTS &amp; SERVICES</a>
  <a style="left:1020px">CONTACT US</a>
  <span class="caret"></span>
</nav>

<section class="hero" role="img" aria-label="Photo of a well-site in winter with a service truck, crane rig and tanker trucks among snowy pine trees"></section>
<div class="hero-dots"><span></span><span></span><span></span><span></span><span></span></div>

<h2 class="section-title challenge-title">THE CHALLANGE</h2>
<svg class="divider" style="top:814px" viewBox="0 0 340 20" aria-hidden="true">
  <line x1="0" y1="10" x2="340" y2="10" stroke="#9fd5ee" stroke-width="1"/>
  <path d="M140 12 C160 2,200 2,215 8 C195 5,165 7,150 13 Z" fill="var(--brand)"/>
</svg>
<p class="challenge-text">It is a long established fact that a reader will be distracted by the readable content of a page when looking at its layout. The point of using Lorem Ipsum is that it has a more-or-less normal distribution of letters, as opposed to using 'Content here, content here', making it look like readable English. Many desktop publishing packages and web page editors now use Lorem Ipsum as their default model text, and a search for 'lorem ipsum' will uncover many web sites still in their infancy.</p>
<a class="btn btn-solid">Learn More</a>

<section class="services-band"></section>
<div class="service" style="left:54px">
  <svg width="56" height="52" viewBox="0 0 56 52" aria-hidden="true">
    <path d="M4 10 L30 4 L34 10 L8 16 Z" fill="var(--brand)"/>
    <path d="M22 8 L16 44 M22 8 L28 44" stroke="var(--brand)" stroke-width="3" fill="none"/>
    <rect x="28" y="34" width="22" height="12" fill="var(--brand)"/>
    <rect x="10" y="44" width="42" height="4" fill="var(--brand)"/>
  </svg>
  Permanent Artificial Lift
</div>
<span class="service-sep" style="left:334px"></span>
<div class="service" style="left:325px">
  <svg width="56" height="52" viewBox="0 0 56 52" aria-hidden="true">
    <circle cx="28" cy="26" r="19" fill="none" stroke="var(--brand)" stroke-width="7" stroke-dasharray="5 3"/>
    <circle cx="28" cy="26" r="14" fill="var(--brand)"/>
    <path d="M20 34 L32 22" stroke="#1e1e1e" stroke-width="4"/>
    <circle cx="34" cy="20" r="5" fill="none" stroke="#1e1e1e" stroke-width="3"/>
  </svg>
  Well Services
</div>
<span class="service-sep" style="left:597px"></span>
<div class="service" style="left:580px">
  <svg width="80" height="52" viewBox="0 0 80 52" aria-hidden="true">
    <path d="M16 50 C6 36,4 30,4 24 a12 12 0 0 1 24 0 c0 6,-2 12,-12 26Z" fill="var(--brand)"/>
    <circle cx="16" cy="24" r="5" fill="#1e1e1e"/>
    <path d="M40 44 C28 28,26 20,26 14 a14 14 0 0 1 28 0 c0 6,-2 14,-14 30Z" fill="var(--brand)"/>
    <circle cx="40" cy="14" r="6" fill="#1e1e1e"/>
    <path d="M64 50 C54 36,52 30,52 24 a12 12 0 0 1 24 0 c0 6,-2 12,-12 26Z" fill="var(--brand)"/>
    <circle cx="64" cy="24" r="5" fill="#1e1e1e"/>
  </svg>
  Locations
</div>
<span class="service-sep" style="left:857px"></span>
<div class="service" style="left:859px">
  <svg width="56" height="52" viewBox="0 0 56 52" aria-hidden="true">
    <circle cx="28" cy="26" r="23" fill="none" stroke="var(--brand)" stroke-width="3"/>
    <path d="M20 14 l6 0 l2 8 l-4 3 c2 5,5 8,9 10 l3 -4 l8 2 l0 6 c-16 2,-28 -12,-24 -25Z" fill="var(--brand)"/>
  </svg>
  Contact Us
</div>

<section class="solution"></section>
<h2 class="section-title solution-title">THE SOLUTION</h2>
<svg class="divider" style="top:1494px" viewBox="0 0 340 20" aria-hidden="true">
  <line x1="0" y1="10" x2="340" y2="10" stroke="#bfe5f7" stroke-width="1"/>
  <path d="M140 12 C160 2,200 2,215 8 C195 5,165 7,150 13 Z" fill="#fff"/>
</svg>
<figure class="solution-figure"><div role="img" aria-label="3D cutaway illustration of rock strata with a horizontal wellbore beneath a grassy surface"></div></figure>
<h3 class="solution-heading">Horizontal &amp; Deviated Wells:</h3>
<span class="solution-rule"></span>
<p class="solution-text" style="top:1620px">With no moving parts, the KVR jet pump takes the industry to the next level, allowing for jet pump placement anywhere in the horizontal profile. Using power fluid as the drive mechanism of a jet pump, the system has no problems with deviated, crooked or horizontal wellbores.</p>
<p class="solution-text" style="top:1729px">With a jet pump landed in the horizontal section of a well, operators are not only able to achieve higher inflow rates, they are also able to achieve higher ultimate reserve recovery</p>
<a class="btn btn-outline">Learn More</a>

<div class="follow-label">Follow Us Now:</div>
<span class="follow-circle" style="left:483px" aria-label="Social network 1"></span>
<span class="follow-circle" style="left:601px" aria-label="Social network 2"></span>
<span class="follow-circle" style="left:720px" aria-label="Social network 3"></span>
<span class="follow-circle" style="left:838px" aria-label="Social network 4"></span>

<footer class="site-footer"></footer>
<div class="footer-heading faint" style="left:140px">ABOUT THE COMPANY</div>
<p class="footer-about">Lorem ipsum dolor sit amet, conse cte tur adipis ici ngal elitm sed do eius mod tempor incid idunt ut labore eta dolo mana aliqua. Ut enim ad minim veniam. Tattooed woolen sweater whatever semiotics, gallery Brookvale VHS viral sustainable bespoke vinyl roof party.</p>

<div class="footer-heading" style="left:354px">CUSTOMER CATE</div>
<span class="footer-rule" style="left:354px;width:238px"></span>
<ul class="footer-links" style="left:354px;top:2208px">
  <li>Contact</li><li>Customer Cate</li><li>Sitemap</li><li>Term &amp; Conditions</li><li>About Us</li><li>Cart</li>
</ul>

<div class="footer-heading" style="left:618px">INFORMATION</div>
<span class="footer-rule" style="left:618px;width:238px"></span>
<ul class="footer-links" style="left:633px;top:2208px">
  <li>What We Do</li><li>Who We Are</li><li>Products &amp; Services</li><li>Where We Operate</li>
</ul>

<div class="footer-heading" style="left:886px">NEWSLETTER</div>
<span class="footer-rule" style="left:886px;width:237px"></span>
<p class="newsletter-text">Subscribe to the Brenmoor Systems mailing list to receive updates on new arrivals, special offers and other discount information.</p>
<div class="email-field">Email Address</div>
<div class="subscribe">Subscribe</div>
<div class="to-top" aria-label="Back to top">
  <svg width="12" height="8" viewBox="0 0 12 8" aria-hidden="true"><path d="M1 7 L6 2 L11 7" stroke="#fff" stroke-width="1.6" fill="none"/></svg>
</div>
<div class="copyright">Copyright © 2018-Brenmoor Systems, All Rights Reserved.</div>

</body>
</html>
```